Jewelers Website

This is for the DESIGN ONLY.
I am a software programmer and will be doing the development.
New website design for
www.lumaoakstones.com.au
Need a fresh new look for an online only jewellery business who produce their jewellery by hand. I would like it designed in a parallax style. Feel free to recommend fonts to use for the site. This is an Australian based company located in NSW so shots of sites in NSW might make nice background images.
http://brixolatemplates.net/demo/#theme=parallax
To contain the below sections
About Us
Contact Us
Gallery
Testimonials
Diamond Types
The colour scheme is to be Black / White and Silver.
With the Parallax style there will be moving sections and images for added impact.
Target Market(s)
Young Adults mainly engagement jewellery
Industry/Entity Type
Software
Look and feel

```html
<!DOCTYPE html>
<html lang="en">
<head>
<meta charset="utf-8">
<title>Lumaoak Stones — Diamond Engagement Rings &amp; Jewellery</title>
<link href="https://fonts.googleapis.com/css2?family=Cormorant+Garamond:wght@500;600&family=Open+Sans:wght@400;600&display=swap" rel="stylesheet">
<style>
:root{
  --ink:#111;
  --header:#232323;
  --paper:#e9e9e9;
  --paper-dark:#dcdcdc;
  --white:#fff;
  --text:#3a3a3a;
  --muted:#8a8a8a;
  --silver:#c9ccd1;
  --line:#3a3a3a;
  --serif:"Cormorant Garamond", Georgia, serif;
  --sans:"Open Sans", Arial, sans-serif;
}
*{box-sizing:border-box;margin:0;padding:0}
html,body{width:1200px;height:3333px;overflow:hidden}
body{position:relative;background:var(--paper);font-family:var(--sans);color:var(--text)}
.abs{position:absolute}

/* header */
.site-header{left:0;top:0;width:1200px;height:94px;background:var(--header)}
.brand{left:40px;top:22px;font-family:var(--serif);font-weight:600;color:var(--white);font-size:22px;line-height:22px;letter-spacing:1px;text-transform:uppercase}
.main-nav{right:0;top:0;height:94px;display:flex}
.main-nav a{display:block;height:94px;line-height:94px;padding:0 24px;color:var(--white);text-decoration:none;font-family:var(--serif);font-size:17px;letter-spacing:.5px;text-transform:uppercase;border-left:1px solid #383838}
.main-nav .menu-toggle{width:110px;display:flex;align-items:center;justify-content:center}

/* hero */
.hero{left:0;top:94px;width:1200px;height:610px;background:radial-gradient(ellipse at 55% 30%,#5a5a5a 0%,#2a2a2a 40%,#0d0d0d 80%)}
.hero-bracelet{left:260px;top:0;width:940px;height:610px;background:radial-gradient(ellipse at 40% 25%,rgba(230,230,235,.35) 0%,rgba(160,160,170,.15) 35%,rgba(0,0,0,0) 65%),radial-gradient(ellipse at 92% 60%,rgba(220,220,228,.3) 0%,rgba(0,0,0,0) 40%)}
.hero-title{left:40px;top:494px;font-family:var(--serif);font-weight:500;color:var(--white);font-size:38px;line-height:48px}
.btn-outline{display:flex;align-items:center;justify-content:space-between;border:2px solid var(--white);border-radius:20px;color:var(--white);font-family:var(--serif);font-size:15px;text-transform:uppercase;letter-spacing:.5px}
.buy-now{left:40px;top:620px;width:147px;height:38px;padding:0 6px 0 18px}
.buy-now .arrow{width:26px;height:26px;border:2px solid var(--white);border-radius:50%;display:flex;align-items:center;justify-content:center}
.social{top:620px;width:38px;height:38px;border:2px solid var(--white);border-radius:50%}
.slider-dots{left:1124px;top:632px;display:flex;gap:6px}
.slider-dots span{width:11px;height:11px;border-radius:50%;background:#888}
.slider-dots span.active{background:var(--white)}

/* section headings */
.heading{font-family:var(--serif);font-weight:500;font-size:36px;text-transform:uppercase;letter-spacing:1px;color:var(--ink)}
.btn-small{display:flex;align-items:center;justify-content:center;border:1px solid #555;border-radius:10px;font-family:var(--serif);font-size:11px;color:#333;background:var(--white)}

/* about */
.about-heading{right:42px;top:780px;text-align:right}
.about-bar{left:998px;top:833px;width:160px;height:15px;background:var(--ink)}
.about-text{right:42px;top:864px;width:560px;text-align:right;font-size:15px;line-height:22px;color:#444}
.about-btn{left:1087px;top:929px;width:71px;height:18px}

/* gallery */
.tile{overflow:hidden}
.tile-caption{position:absolute;left:0;bottom:0;width:100%;height:58px;background:rgba(0,0,0,.55);color:var(--white);font-family:var(--serif);font-size:18px;display:flex;align-items:center;justify-content:center}
.tile-feature{left:42px;top:1016px;width:271px;height:477px;background:linear-gradient(180deg,#3c7fc7 0%,#7fb0dc 35%,#cfe0d8 55%,#5e8a4a 80%,#7b8f55 100%)}
.gallery-heading{left:18px;top:46px;color:var(--white);font-size:32px}
.gallery-bar{position:absolute;left:18px;top:102px;width:152px;height:17px;background:var(--white)}
.gallery-text{position:absolute;left:18px;top:136px;width:190px;color:var(--white);font-size:15px;line-height:20px}
.gallery-btn{position:absolute;left:18px;top:238px;width:70px;height:18px;background:transparent;border-color:var(--white);color:var(--white)}

/* testimonials */
.testi-heading{left:0;top:1574px;width:1200px;text-align:center;color:#222}
.divider{left:524px;top:1632px}
.testi-text{left:84px;top:1672px;width:1032px;text-align:center;font-size:16px;line-height:25px;color:#444}
.learn-more{left:0;top:1756px;width:1200px;text-align:center;font-size:16px;color:#333;text-decoration:underline}
.avatar{top:1827px;width:146px;height:146px;border-radius:50%;border:7px solid var(--white);box-shadow:0 2px 6px rgba(0,0,0,.25)}
.avatar.current{border-color:#2a2a2a}

/* diamond types */
.types{left:0;top:2073px;width:1200px;height:765px;background:radial-gradient(ellipse at 50% 40%,#1c1c1c 0%,#060606 75%)}
.types-heading{left:0;top:2196px;width:1200px;text-align:center;color:var(--white)}
.types-bar{left:464px;top:2255px;width:272px;height:18px;background:var(--white)}
.types-sub{left:0;top:2288px;width:1200px;text-align:center;color:var(--white);font-size:20px;line-height:26px}
.types-text{left:367px;top:2356px;width:466px;text-align:center;color:#ddd;font-size:11px;line-height:14px}
.cut{top:2440px;width:98px;height:182px;border:1px solid #3a3a3a;text-align:center}
.gem{margin:14px auto 0;width:60px;height:60px;background:radial-gradient(circle at 40% 35%,#ffffff 0%,#c9d6e6 45%,#7d8fa6 100%)}
.cut-label{margin-top:20px;color:#ccc;font-size:13px;line-height:16px}
.types-btn{left:564px;top:2669px;width:72px;height:18px;background:transparent;border-color:#888;color:#ccc}

/* footer */
.copyright{left:0;top:2886px;width:1200px;text-align:center;font-size:11px;color:#333}
.footer-nav{left:0;top:2912px;width:1200px;text-align:center;font-size:11px;color:#333}
.office-switch{left:493px;top:2949px;width:214px;height:38px;border-radius:19px;background:var(--white);display:flex;font-size:13px}
.office-switch span{flex:1;display:flex;align-items:center;justify-content:center;color:#999;border-radius:19px}
.office-switch .on{background:var(--ink);color:var(--white)}
.map{left:0;top:3018px;width:1200px;height:280px;background:linear-gradient(90deg,#e8e4d8 0%,#ede7d2 45%,#d9d6cc 70%,#a8c1dc 82%,#9fbbd9 100%)}
.contact-bar{left:0;top:3298px;width:1200px;height:35px;background:#eee;display:flex;align-items:center;font-size:13px;color:#333}
.contact-bar .item{display:flex;align-items:center;gap:6px;margin-left:40px}
.contact-btn{left:1088px;top:3306px;width:70px;height:18px}
</style>
</head>
<body>

<header class="site-header abs">
  <div class="brand abs">Lumaoak<br>Stones</div>
  <nav class="main-nav abs">
    <a href="#about">About Us</a>
    <a href="#contact">Contact Us</a>
    <a href="#gallery">Gallery</a>
    <a href="#testimonials">Testimonials</a>
    <a href="#types">Diamond Types</a>
    <a class="menu-toggle" href="#menu" aria-label="Menu">
      <svg width="24" height="18" viewBox="0 0 24 18"><rect y="1" width="24" height="3" fill="#fff"/><rect y="8" width="24" height="3" fill="#fff"/><rect y="15" width="24" height="3" fill="#fff"/></svg>
    </a>
  </nav>
</header>

<section class="hero abs">
  <div class="hero-bracelet abs" role="img" aria-label="Close-up photograph of a silver diamond bangle on a dark sparkling background"></div>
</section>
<h1 class="hero-title abs">Diamond Engagement<br>Rings &amp; Jewellery</h1>
<a class="btn-outline buy-now abs" href="#shop">Buy Now
  <span class="arrow"><svg width="10" height="12" viewBox="0 0 10 12"><path d="M3 1l5 5-5 5" stroke="#fff" stroke-width="2" fill="none"/></svg></span>
</a>
<a class="social abs" style="left:201px" href="#social-1" aria-label="Social network link"></a>
<a class="social abs" style="left:243px" href="#social-2" aria-label="Social network link"></a>
<a class="social abs" style="left:288px" href="#social-3" aria-label="Social network link"></a>
<div class="slider-dots abs"><span></span><span class="active"></span></div>

<section id="about">
  <h2 class="heading about-heading abs">About Us</h2>
  <div class="about-bar abs"></div>
  <p class="about-text abs">Lorem ipsum dolor sit amet, conse ctetur adipisicing elit, sed do eius mod tempor incididunt ut labore et dolore magna aliqua.</p>
  <a class="btn-small about-btn abs" href="#about-more">Click Here</a>
</section>

<section id="gallery">
  <div class="tile tile-feature abs" role="img" aria-label="Photograph of a wedding couple on a palm-lined tropical path">
    <h2 class="heading gallery-heading abs">Gallery</h2>
    <div class="gallery-bar"></div>
    <p class="gallery-text">Lorem ipsum dolor sit amet, consectetur adipi sicing elit, sed do eiusmod tempor incididunt</p>
    <a class="btn-small gallery-btn" href="#gallery-more">Click Here</a>
  </div>
  <div class="tile abs" style="left:324px;top:1016px;width:269px;height:233px;background:linear-gradient(160deg,#c9d4e0,#8ea0b4 60%,#5f7084)" role="img" aria-label="Photograph of a marquise diamond ring">
    <div class="tile-caption">Lorem Ipsum</div></div>
  <div class="tile abs" style="left:607px;top:1016px;width:269px;height:233px;background:linear-gradient(160deg,#d8b6a2,#b89080 55%,#6d5a52)" role="img" aria-label="Photograph of a diamond ring worn on a finger">
    <div class="tile-caption">Lorem Ipsum</div></div>
  <div class="tile abs" style="left:889px;top:1016px;width:269px;height:477px;background:radial-gradient(ellipse at 40% 35%,#b9c2c8 0%,#5e6b72 45%,#232b30 100%)" role="img" aria-label="Close-up photograph of a solitaire diamond ring">
    <div class="tile-caption">Lorem Ipsum</div></div>
  <div class="tile abs" style="left:324px;top:1260px;width:269px;height:233px;background:linear-gradient(160deg,#4a3a5c,#2e2340 50%,#1a4d3a)" role="img" aria-label="Photograph of an emerald and diamond necklace on purple fabric">
    <div class="tile-caption">Lorem Ipsum</div></div>
  <div class="tile abs" style="left:607px;top:1260px;width:269px;height:233px;background:linear-gradient(180deg,#f4f4f4,#bfc4c0 45%,#2f5a44 70%,#1c1c1c)" role="img" aria-label="Photograph of an emerald and gold bracelet">
    <div class="tile-caption">Lorem Ipsum</div></div>
</section>

<section id="testimonials">
  <h2 class="heading testi-heading abs">Daniel &amp; Clarissa</h2>
  <svg class="divider abs" width="145" height="24" viewBox="0 0 145 24" aria-hidden="true">
    <rect x="0" y="11" width="145" height="3" fill="#111"/>
    <circle cx="72.5" cy="12" r="12" fill="#111"/>
    <circle cx="72.5" cy="12" r="7" fill="none" stroke="#fff" stroke-width="1"/>
  </svg>
  <p class="testi-text abs">Daniel and I met at a mutual friend's 16th Birthday Party in 2005. We immediately became good friends and by June 2006 we were officially dating. Daniel and I also went to school next door to each other so we got through the stresses of year 11 and 12 together. Daniel proposed to me in December 2010 at my favourite picnic...</p>
  <a class="learn-more abs" href="#testimonial-more">Learn More</a>
  <div class="avatar current abs" style="left:358px;background:linear-gradient(160deg,#d9d4cc,#9a8f84 60%,#4d4640)" role="img" aria-label="Wedding photograph of the couple"></div>
  <div class="avatar abs" style="left:527px;background:linear-gradient(160deg,#6f7f8c,#3a4650 60%,#1e252b)" role="img" aria-label="Photograph of the couple in a wedding car"></div>
  <div class="avatar abs" style="left:698px;background:linear-gradient(160deg,#efe4da,#b79f8c 55%,#5e4a3d)" role="img" aria-label="Close portrait photograph of the bride and groom"></div>
</section>

<section id="types" class="types abs"></section>
<h2 class="heading types-heading abs">Diamond Types</h2>
<div class="types-bar abs"></div>
<p class="types-sub abs">Choosing the cut and shape<br>of Diamond</p>
<p class="types-text abs">When people talk about the cut of a diamond, they tend to refer on how a diamond is shaped and polished, the way its sides or facets are designed and how shallowly or deeply it has been cut.</p>

<div class="cut abs" style="left:333px">
  <div class="gem" style="border-radius:50%" role="img" aria-label="Round brilliant cut diamond"></div>
  <div class="cut-label">Round<br>Brilliant</div></div>
<div class="cut abs" style="left:442px">
  <div class="gem" style="border-radius:16px" role="img" aria-label="Cushion cut diamond"></div>
  <div class="cut-label">Cushion<br>Cut</div></div>
<div class="cut abs" style="left:551px">
  <div class="gem" style="width:44px;border-radius:50%" role="img" aria-label="Oval cut diamond"></div>
  <div class="cut-label">Oval</div></div>
<div class="cut abs" style="left:660px">
  <div class="gem" style="width:52px;height:52px;margin-top:18px" role="img" aria-label="Princess cut diamond"></div>
  <div class="cut-label" style="margin-top:24px">Princess</div></div>
<div class="cut abs" style="left:769px">
  <svg style="display:block;margin:14px auto 0" width="60" height="60" viewBox="0 0 60 60" role="img" aria-label="Heart cut diamond">
    <defs><radialGradient id="heartGem" cx="40%" cy="35%" r="70%"><stop offset="0" stop-color="#fff"/><stop offset=".45" stop-color="#c9d6e6"/><stop offset="1" stop-color="#7d8fa6"/></radialGradient></defs>
    <path d="M30 56C14 42 2 32 2 18 2 8 10 2 18 2c6 0 10 3 12 8 2-5 6-8 12-8 8 0 16 6 16 16 0 14-12 24-28 38z" fill="url(#heartGem)"/>
  </svg>
  <div class="cut-label">Heart</div></div>
<a class="btn-small types-btn abs" href="#types-more">Click Here</a>

<footer id="contact">
  <p class="copyright abs">© Copyright 2014 Lumaoak Stones Pty Ltd</p>
  <p class="footer-nav abs">About Us &nbsp;-&nbsp; Contact Us &nbsp;-&nbsp; Gallery &nbsp;-&nbsp; Testimonials &nbsp;-&nbsp; Diamond Types</p>
  <div class="office-switch abs"><span class="on">Sydney</span><span>Germany</span></div>
  <div class="map abs" role="img" aria-label="Street map of Sydney with the showroom location marked"></div>
  <div class="contact-bar abs">
    <span class="item">
      <svg width="10" height="14" viewBox="0 0 10 14"><path d="M5 0a5 5 0 0 0-5 5c0 4 5 9 5 9s5-5 5-9a5 5 0 0 0-5-5zm0 7a2 2 0 1 1 0-4 2 2 0 0 1 0 4z" fill="#222"/></svg>
      Marrickvale NSW 2299, Australia</span>
    <span class="item">
      <svg width="13" height="13" viewBox="0 0 24 24"><path d="M6.6 10.8a15 15 0 0 0 6.6 6.6l2.2-2.2c.3-.3.7-.4 1-.2 1.1.4 2.3.6 3.6.6.6 0 1 .4 1 1V20c0 .6-.4 1-1 1A17 17 0 0 1 3 4c0-.6.4-1 1-1h3.5c.6 0 1 .4 1 1 0 1.3.2 2.5.6 3.6.1.3 0 .7-.2 1z" fill="#222"/></svg>
      +61 (0)2 9000 4821</span>
  </div>
  <a class="btn-small contact-btn abs" href="#contact-more">Click Here</a>
</footer>

</body>
</html>
```